Business Card template designs

We need a lot of Business card designs.
Your designs will get exposure on our newly opened business-card printing website.
We are committed to quality of paper and packages we use, so they will come up very fancy.

Here is your advantage. We will put the profile of the graphic designer on our site so that you can showcase your designs to people around the world and in Japan.

A profile is not mandatory, although we encourage graphic designers to have a profile to get continuous work in the future.
We are looking forward to having many good designs.

The right of the use of design will be owned by us.
The design may be used to the products other than
business cards.

Target Market(s)

designer,photographer,creator,artist

Industry/Entity Type

Printing

Contact Information for Business Card

The back design is important.
Please check the reference file.

Requirements
Must have
• Please include the following, required information on your business card designs.
• Name: Haruna Okabe
• Title: Designer
• Web: https://www.ketori.co.jp/kt/
• Address: 4-17 Kamiharuta-Cho Meguro-ku, Tokyo
• Email: info@kketori.com
• Phone: 03 4816 3907
• Mobile: 070 2143 6658
• * For Japanese sites, we will convert the text portion to Japanese characters.
• * In case of 28mmx70mm only include Name,Enail,Phone and SNS account(https://www.facebook.com/kketori.com)
• 1. colorful
• 2. simple
• 3. natural
• 4. modern
• 5. cool
• 6. sporty
• Please make variations of the same image with 3-6
• different colors / patterns for one design so that
• customers can compare and choose.
• If you want to use a same picture, please make make
• copies and paste on each different types of design.
Nice to have
• You may also use, the following non-required information.
• Company Name: Ketori, Inc.
• Fax: 03-4173-9620
• Open space for company logo

```html
<!DOCTYPE html>
<html lang="en">
<head>
<meta charset="utf-8">
<title>Business Card – Haruna Okabe</title>
<link rel="stylesheet" href="https://fonts.googleapis.com/css2?family=Mulish:wght@400;700&display=swap">
<style>
  :root {
    --page-bg: #d9d6d2;
    --card-frost-top: #f3f4f6;
    --card-frost-bottom: #e4e7ea;
    --navy: #1a1f6b;
    --navy-deep: #0e1250;
    --navy-light: #2a3190;
    --text-main: #2c3350;
    --text-muted: #555a66;
    --silver: #e3e6ee;
  }
  * { box-sizing: border-box; margin: 0; padding: 0; }
  html, body {
    width: 1200px; height: 969px; overflow: hidden;
    background: var(--page-bg);
    font-family: "Mulish", "Century Gothic", sans-serif;
  }
  .card {
    position: absolute; left: 100px; top: 200px;
    width: 1000px; height: 570px;
    border-radius: 22px; overflow: hidden;
    background: linear-gradient(160deg, var(--card-frost-top), var(--card-frost-bottom));
    box-shadow: 0 10px 30px rgba(0,0,0,0.18);
  }
  .card__wave { position: absolute; inset: 0; width: 1000px; height: 570px; }
  .card__brand {
    position: absolute; left: 640px; top: 72px;
    display: flex; align-items: center; gap: 16px;
    color: var(--silver); font-size: 74px; font-weight: 400; letter-spacing: 1px;
  }
  .card__brand-dot {
    width: 22px; height: 22px; border-radius: 50%; background: var(--silver);
  }
  .holder { position: absolute; left: 48px; top: 28px; }
  .holder__name { font-size: 34px; font-weight: 700; color: var(--navy); line-height: 1.1; }
  .holder__title { font-size: 26px; color: var(--text-muted); margin-top: 2px; }
  .address {
    position: absolute; left: 52px; top: 226px;
    font-size: 26px; line-height: 36px; color: var(--text-main);
  }
  .contacts {
    position: absolute; left: 52px; top: 366px; list-style: none;
    font-size: 25px; line-height: 35px; color: var(--text-main);
  }
  .contacts__item { display: flex; align-items: center; gap: 12px; }
  .contacts__icon { width: 22px; height: 22px; fill: var(--navy); flex: none; }
</style>
</head>
<body>
  <div class="card">
    <svg class="card__wave" viewBox="0 0 1000 570" aria-hidden="true">
      <defs>
        <linearGradient id="navyFill" x1="0" y1="0" x2="1" y2="1">
          <stop offset="0" stop-color="var(--navy-deep)"/>
          <stop offset="0.55" stop-color="var(--navy-light)"/>
          <stop offset="1" stop-color="var(--navy-deep)"/>
        </linearGradient>
      </defs>
      <path d="M445,0 C460,250 610,450 830,570 L1000,570 L1000,0 Z" fill="url(#navyFill)"/>
      <path d="M462,205 C520,360 640,480 800,570" fill="none" stroke="var(--silver)" stroke-width="5" stroke-linecap="round"/>
    </svg>

    <div class="card__brand"><span class="card__brand-dot"></span>Ketori</div>

    <div class="holder">
      <p class="holder__name">Haruna Okabe</p>
      <p class="holder__title">Designer</p>
    </div>

    <address class="address" style="font-style:normal">
      Ketori, Inc.<br>
      4-17 Kamiharuta-Cho<br>
      Meguro-ku, Tokyo
    </address>

    <ul class="contacts">
      <li class="contacts__item">
        <svg class="contacts__icon" viewBox="0 0 24 24"><path d="M6.6 10.8a15.1 15.1 0 0 0 6.6 6.6l2.2-2.2a1 1 0 0 1 1-.25 11.4 11.4 0 0 0 3.6.57 1 1 0 0 1 1 1V20a1 1 0 0 1-1 1A17 17 0 0 1 3 4a1 1 0 0 1 1-1h3.5a1 1 0 0 1 1 1c0 1.25.2 2.45.57 3.6a1 1 0 0 1-.25 1z"/></svg>
        03 4816 3907
      </li>
      <li class="contacts__item">
        <svg class="contacts__icon" viewBox="0 0 24 24"><path d="M7 1h10a2 2 0 0 1 2 2v18a2 2 0 0 1-2 2H7a2 2 0 0 1-2-2V3a2 2 0 0 1 2-2zm0 3v14h10V4zm5 15.5a1.2 1.2 0 1 0 0 2.4 1.2 1.2 0 0 0 0-2.4z"/></svg>
        070 2143 6658
      </li>
      <li class="contacts__item">
        <svg class="contacts__icon" viewBox="0 0 24 24"><path d="M6 2h9l3 3v4h1a3 3 0 0 1 3 3v7H2v-7a3 3 0 0 1 3-3h1zm2 2v5h8V6h-2V4zM5 13v2h14v-2zM4 20h16v2H4z"/></svg>
        03-4173-9620
      </li>
      <li class="contacts__item">
        <svg class="contacts__icon" viewBox="0 0 24 24"><path d="M2 5h20v14H2zm2 2v.5l8 5 8-5V7zm0 3v7h16v-7l-8 5z"/></svg>
        info@kketori.com
      </li>
      <li class="contacts__item">
        <svg class="contacts__icon" viewBox="0 0 24 24"><path d="M12 2a10 10 0 1 0 0 20 10 10 0 0 0 0-20zm0 2a8 8 0 0 1 5.3 2H14l-1 2 2 2-1 3h-3l-2-2-3 1A8 8 0 0 1 12 4zm1 15.9V17l3-2 3 1a8 8 0 0 1-6 3.9z"/></svg>
        www.ketori.co.jp/kt
      </li>
    </ul>
  </div>
</body>
</html>
```